Corporate flyer highlighting service offering for PR agency

A corporate flyer is needed for a new service offering that we are doing. The product name is HarborLeap it is a marketing and communications services offering for companies who are getting ready to sell their business. If we are really happy with the designer's work, there will be a great deal more projects. I am looking for a clean design with a few pops of color from my site. https://quillmarsh.partners. I am looking for a good design with data in sections. I am looking for a clean design that feels high-end but not cluttered. Please do not use images of people. Please see the following examples of types of designs I like.
https://www.tackboard.example/pin/839201746530918264/
https://www.tackboard.example/pin/402918375561029847/
https://assets.stockvale.example/corporate-flyer-template-KRTPMB
https://designbrook.example/item/corporate-flyer-template/81046395?s_rank=8
https://assets.stockvale.example/corporate-business-flyer-template-93PX7D

I had to place the project on hold as I choose the wrong type of project and did not get many designs as a result. I am reposting this with an updated brief.

Target Market(s)

Business sellers and brokers

Industry/Entity Type

Marketing for business sellers

Font styles to use
Sans Serif

Requirements
Must have
• Good quality design with content in sections. Clean and high end feeling is a must.
Should not have
• A lot of images of people.

```html
<!DOCTYPE html>
<html lang="en">
<head>
<meta charset="utf-8">
<title>HarborLeap Flyer – Quillmarsh Partners</title>
<link rel="stylesheet" href="https://fonts.googleapis.com/css2?family=Poppins:ital,wght@0,300;0,400;0,500;0,600;0,700;1,400;1,500&display=swap">
<style>
:root{
  --backdrop:#bdbdbd;
  --paper:#ffffff;
  --blue:#1c80c6;
  --blue-deep:#0f69ab;
  --blue-head:#1a7cc1;
  --orange:#f39c1f;
  --orange-light:#fcd28a;
  --alert:#e8532b;
  --green:#8dc63f;
  --ink:#4a4a4a;
  --ink-dark:#2d2d2d;
  --band:#ececec;
}
*{margin:0;padding:0;box-sizing:border-box}
html,body{width:1200px;height:1117px;overflow:hidden;background:var(--backdrop)}
body{position:relative;font-family:"Poppins",Arial,sans-serif;color:var(--ink);font-weight:300}
.page{position:absolute;width:358px;height:505px;background:var(--paper);overflow:hidden}
.page--cover{left:232px;top:44px}
.page--valuation{left:610px;top:44px}
.page--marketing{left:232px;top:568px}
.page--review{left:610px;top:568px}
.abs{position:absolute}
.page-foot{position:absolute;left:0;right:0;bottom:0;height:7px;background:linear-gradient(90deg,var(--orange) 0%,var(--orange) 40%,var(--orange-light) 55%,var(--orange) 70%)}
.copy{font-size:6.6px;line-height:8.6px}
.center{text-align:center}
.section-title{font-size:8.6px;font-weight:500;color:var(--blue-head);line-height:11px}
.ticks{list-style:none;font-size:6.6px;line-height:8.6px}
.ticks li{position:relative;padding-left:11px}
.ticks li::before{content:"";position:absolute;left:0;top:1.6px;width:5px;height:5px;border:1.2px solid var(--alert);border-radius:50%}
.ticks li::after{content:"";position:absolute;left:1.6px;top:3.1px;width:2px;height:1px;border-left:1px solid var(--alert);border-bottom:1px solid var(--alert);transform:rotate(-45deg)}
.ticks b{font-weight:600;color:var(--ink-dark)}

/* cover */
.brand{left:22px;top:38px;display:flex;align-items:center;gap:6px}
.brand-square{width:12px;height:12px;background:var(--blue)}
.brand-name{font-size:11px;font-weight:600;color:var(--ink-dark);letter-spacing:.3px;line-height:12px}
.cover-band{left:0;top:98px;width:358px;height:107px;background:var(--blue)}
.cover-art{left:0;top:0}
.cover-title{left:22px;top:111px;color:#fff;font-size:10.9px;font-weight:600;line-height:12.3px;white-space:nowrap;z-index:2}
.cover-title .product{display:block;color:var(--green);font-size:15px;line-height:17px;font-weight:600}
.cover-stripe{left:0;top:205px;width:358px;height:12px;background:linear-gradient(180deg,#fff 0 30%,#6fb6e6 30% 75%,#fff 75%)}
.intro-col{top:232px;width:140px;font-size:6.6px;line-height:8.4px}
.intro-divider{left:173px;top:232px;width:1px;height:52px;background:#d2d2d2}
.stat-box{left:24px;width:309px;border:1.5px solid var(--alert);font-size:6.2px;line-height:9.4px;text-align:center;padding:7px 14px}
.stat-box i{font-style:italic}
.stat-box .source{font-weight:500;color:var(--ink-dark);font-style:normal}
.offer-list{left:0;width:358px;top:419px;font-size:6.4px;text-align:center;color:var(--ink-dark);font-weight:400}
.offer-list span::after{content:"•";color:var(--green);margin:0 4px}
.offer-list span:last-child::after{content:""}
.gray-band{left:0;width:358px;background:var(--band)}

/* valuation */
.top-blue{left:0;top:0;width:358px;height:112px;background:var(--blue)}
.blue-copy{color:#fff}
.orange-callout{left:16px;top:87px;width:326px;height:51px;background:var(--orange);border:3px solid #fff;color:#fff;font-weight:600;font-size:6.5px;line-height:8.7px;text-align:center;padding:5px 6px}
.rule{left:18px;width:322px;height:1.5px;background:#e2e2e2}

/* marketing */
.stat-frame{left:24px;width:308px;border:1.5px solid #fff;color:#fff;text-align:center;font-size:6.8px;line-height:8.8px;padding:8px 8px}
.stat-frame .link{display:block;margin-top:8px;font-weight:500}
.col-divider{width:1px;background:#cfcfcf}

/* review */
.quote-box{left:24px;top:155px;width:309px;height:39px;border:1.5px solid var(--alert);text-align:center;font-style:italic;font-size:8.2px;line-height:12px;color:var(--ink-dark);padding:6px 20px 0}
.quote-box b{font-weight:600}
.bottom-blue{left:0;top:348px;width:358px;height:150px;background:linear-gradient(135deg,var(--blue) 0%,var(--blue-deep) 100%)}
.bottom-blue .copy{position:absolute;color:#fff;width:148px}
</style>
</head>
<body>

<!-- Page 1: cover -->
<section class="page page--cover">
  <div class="abs brand"><span class="brand-square"></span><span class="brand-name">QUILLMARSH<br>PARTNERS</span></div>
  <div class="abs cover-band"></div>
  <svg class="abs cover-art" width="358" height="210" viewBox="0 0 358 210">
    <defs>
      <linearGradient id="skyline" x1="0" y1="0" x2="0" y2="1">
        <stop offset="0" stop-color="#c9d6e0"/>
        <stop offset=".45" stop-color="#b8a58a"/>
        <stop offset="1" stop-color="#5a5650"/>
      </linearGradient>
    </defs>
    <polygon points="305,0 358,0 358,95" fill="var(--orange)"/>
    <polygon points="196,0 318,0 356,70 296,195 206,195 162,100" fill="#fff"/>
    <polygon role="img" aria-label="City skyline photograph at sunrise" points="201,4 314,4 350,70 292,190 210,190 169,100" fill="url(#skyline)"/>
  </svg>
  <h1 class="abs cover-title"><span class="product">HarborLeap</span>provides executives<br>and business owners<br>with clear guidance<br>to unlock non-financial<br>value ahead of an exit.</h1>
  <div class="abs cover-stripe"></div>

  <p class="abs intro-col" style="left:22px">A strong communication and marketing strategy can significantly increase the value of your business leading up to an exit. Buyers are looking to mitigate risk and unlock potential value as a catalyst for clear growth potential.</p>
  <div class="abs intro-divider"></div>
  <p class="abs intro-col" style="left:189px;width:148px">Highlighting your company’s success in the marketplace, identifying, and mitigating reptation risks before buyers do, enhancing employee engagement, finding hidden opportunities to boost marketing KPIs and showcasing IP, data, and innovation, can make a significant difference in valuation.</p>

  <div class="abs stat-box" style="top:304px;height:56px"><i>US institutional investors believe that Investor Relations (IR) accounts for a total variance of 30% in a company’s valuation – from a premium of 10% for “superb” IR to a discount of 20% for “poor” IR.</i><br><span class="source">Corvell Research Group, “Harnessing IR’s Power to Impact a Company’s Valuation.”</span></div>

  <p class="abs copy center" style="left:22px;width:314px;top:374px">We design and implement communication and marketing strategies that deliver significant increases in brand awareness, identify reputational risks, and enhance brand perception, helping owners and investors to realize premium values for their companies. We support owners and companies through:</p>
  <p class="abs offer-list"><span>Company Exit Preparation</span><span>M&amp;A</span><span>IPO</span><span>Spinoff/Divestiture</span><span>New Leadership/Investor</span></p>

  <div class="abs gray-band" style="top:435px;height:58px"></div>
  <p class="abs copy center" style="left:26px;width:306px;top:446px">Few sellers would list their home without first inspecting, repairing broken items, and making updates to highlight the positive aspects --increasing appeal to buyers. However, countless business owners leave money on the table during corporate exits due to a lack of preparation.</p>
  <div class="page-foot"></div>
</section>

<!-- Page 2: valuation -->
<section class="page page--valuation">
  <div class="abs top-blue"></div>
  <p class="abs copy center blue-copy" style="left:26px;width:306px;top:24px">Our team of executive-level communications and marketing experts brings deep buy and sell-side experience. We have played critical roles in the acquisition, integration, and disposition process. Our mix of financial services expertise combined with decades of experience leading internal and external communications, marketing and investor relations teams gives us a unique perspective on identifying and unlocking non-financial areas of value and mitigating non-financial risks before exit.</p>
  <p class="abs orange-callout">While accounting and investment banking teams are hard at work increasing value from a financial perspective, we help organizations enhance their valuation by identifying areas that will appeal most to buyers and ensuring those elements of your business are visible and memorable to those who matter most.</p>

  <h2 class="abs section-title" style="left:29px;top:148px">We help companies increase valuation by:</h2>
  <ul class="abs ticks" style="left:29px;top:164px;width:300px">
    <li style="margin-bottom:7px">Highlighting value in a clear and visible way</li>
    <li style="margin-bottom:7px">Streamlining the exit process</li>
    <li style="margin-bottom:7px">Identifying potential risks and suggesting mitigation measures</li>
    <li>Creating a polished presence in the market ahead of buyer interest</li>
  </ul>
  <div class="abs rule" style="top:232px"></div>

  <p class="abs copy center" style="left:34px;width:290px;top:247px">HarborLeap provides executives and business owners with clear guidance to unlock value ahead of an exit. Our non-disruptive, ala-carte process enables us to work with sellers on specific areas or to do a complete analysis and recommendation and can include:</p>

  <h2 class="abs section-title" style="left:29px;top:294px">Brand Analysis and Recommendations</h2>
  <p class="abs copy" style="left:29px;width:300px;top:308px">Strong brands command a higher valuation. We conduct a brand analysis, providing clear and detailed recommendations to enhance your value proposition and help you stand out from the crowd:</p>
  <ul class="abs ticks" style="left:29px;top:343px;width:316px">
    <li style="margin-bottom:9px">Current external position among competitors --We look at how your brand measures up based on external competitive analysis, positioning in the media and analyst community, and across other digital channels.</li>
    <li style="margin-bottom:9px">Physical brand image--A little bit of paint and updated fixtures can go a long way when increasing the value of a home. The same is true for businesses. Our audit evaluates non-disruptive steps your company can take to enhance your brand look and feel before sale.</li>
    <li style="margin-bottom:9px">Employee brand perception--We conduct a high-level external audit with recommendations to enhance engagement for current and prospective employees.</li>
    <li>Customer brand perception-- We conduct a high-level external audit showcasing how customers perceive your brand in the market. We then provide recommendations for enhancing engagement and maximizing value.</li>
  </ul>
  <div class="page-foot"></div>
</section>

<!-- Page 3: marketing -->
<section class="page page--marketing">
  <div class="abs top-blue" style="height:144px;background:linear-gradient(135deg,var(--blue),var(--blue-deep))"></div>
  <div class="abs stat-frame" style="top:13px;height:55px">A 5% increase in customer retention correlates with at least a 25% increase in profit, according to an analysis by Brandt &amp; Company.<span class="link">(https://media.brandtco.example/Images/BC_Prescription_cutting_costs.pdf)</span></div>
  <div class="abs stat-frame" style="top:77px;height:54px">It costs 5 times more to acquire a new customer than to retain a current one and 16 times more to get new customers to the same spending level as existing ones.<span class="link">(https://growthledger.example/customer-retention-guide-statistics/)</span></div>

  <h2 class="abs section-title" style="left:27px;top:153px">Digital and Traditional Marketing Analysis and Recommendations</h2>
  <p class="abs copy" style="left:27px;width:306px;top:168px">How much money are you leaving on the table? Our marketing audits help organizations identify areas of hidden value that can have significant impacts on revenue and valuation. We optimize current activities and uncover new strategies to increase the effectiveness of current marketing spend. Areas we evaluate include:</p>
  <ul class="abs ticks" style="left:29px;top:211px;width:140px;line-height:10.3px">
    <li>Website traffic and conversion</li>
    <li>CRM process review to identify strategies and recommendations to increase conversion and reactive old-leads</li>
    <li>Email marketing strategy</li>
  </ul>
  <div class="abs col-divider" style="left:182px;top:212px;height:54px"></div>
  <ul class="abs ticks" style="left:203px;top:211px;width:140px;line-height:10.3px">
    <li>Automations and drip marketing</li>
    <li>Social media strategy /presence</li>
    <li>Partnership marketing</li>
    <li>Paid media analysis/strategy suggestion</li>
  </ul>

  <h2 class="abs section-title" style="left:27px;top:281px">Messaging and Content Strategy Review and Analysis</h2>
  <p class="abs copy" style="left:27px;width:306px;top:296px">It’s about your valuation. Full and fair valuation requires a clear, compelling investment case articulated consistently to the right audience at the right time. Messaging to maximize your value in an acquisition or an IPO is quite different from typical selling messages for prospects, customers, or ‘features &amp; business benefits’ for press and analysts. We understand the issues and speak the right language to maximize perception of value with key decision makers.</p>
  <ul class="abs ticks" style="left:29px;top:355px;width:135px">
    <li style="margin-bottom:9px">Review and recommendations of key messaging and value proposition</li>
    <li>Analysis and recommendations to position key executives likely to remain with the company as thought leaders to help build value</li>
  </ul>
  <div class="abs col-divider" style="left:182px;top:358px;height:60px"></div>
  <ul class="abs ticks" style="left:194px;top:355px;width:140px">
    <li style="margin-bottom:9px">Analysis and recommendations to highlight data, IP, and innovation</li>
    <li>Analysis and recommendations to build employee engagement and retention enhancing your most valuable asset--your team</li>
  </ul>

  <div class="abs gray-band" style="top:424px;height:74px"></div>
  <h2 class="abs section-title" style="left:27px;top:430px">Media and Analyst Strategy Development</h2>
  <p class="abs copy" style="left:27px;width:314px;top:445px">Positive articles and inclusion in analyst reports pack a powerful punch when preparing your business for sale. We work with clients to develop a media strategy that goes beyond brand awareness, leveraging media to build a digital history of third-party validation targeted to enhance appeal to prospective buyers while generating traffic and connections, to enhance overall value.</p>
  <div class="page-foot"></div>
</section>

<!-- Page 4: review -->
<section class="page page--review">
  <div class="abs gray-band" style="top:0;height:80px;background:linear-gradient(180deg,#fff,var(--band))"></div>
  <ul class="abs ticks" style="left:29px;top:21px;width:310px;line-height:10.4px">
    <li>Positioning to media and analyst community creating third party market validation</li>
    <li>Key angle recommendations</li>
    <li>Announcement timeline and strategy planning to maximize media value of news</li>
    <li>What is newsworthy</li>
    <li>How to position that news for the most significant impact</li>
  </ul>

  <h2 class="abs section-title" style="left:29px;top:87px">“White Hat/Black Hat Review”</h2>
  <p class="abs copy" style="left:29px;width:300px;top:102px">We take a buyer’s communications and marketing approach to analyzing the client company and provide a “punch list” of things a potential buyer is likely to ask/request in due diligence from a comms/culture/marketing/reputation standpoint to ensure that when potential buyers start screening for sellers and evaluating them, the client company has the upper hand.</p>
  <p class="abs quote-box">“Strategy without tactics is the slowest route to victory. Tactics without strategy is the noise before defeat.” <b>– Oren Valcourt</b></p>
  <p class="abs copy" style="left:29px;width:304px;top:202px">Once the analysis is complete, we deliver actionable intelligence and recommendations to help leaders identify and quickly unlock areas that will boost value and appeal to prospective buyers. Work products include:</p>
  <ul class="abs ticks" style="left:29px;top:239px;width:304px;line-height:10.3px">
    <li style="margin-bottom:10px"><b>Gap Assessment</b> - We provide a comprehensive seller report providing analysis and actionable recommendations to increase your valuation while identifying and mitigating non-financial risks.</li>
    <li><b>Strategic Roadmap</b> - Clients are given an actionable tactical roadmap based on the recommendation provided. Organizations can choose to implement key areas or include this powerful guide as part of their presentation to prospective buyers to highlight latent potential. The roadmap provides actionable steps buyers can take upon close as they make their case for your business with their investment committees.</li>
  </ul>

  <div class="abs bottom-blue">
    <p class="copy" style="left:29px;top:14px">Once the strategy integration roadmap is complete, your team can implement it onyour timeline, we can work with your team providing guidance and executive-level support, or we can fully execute deliverables with our robust capabilities and team.</p>
    <p class="copy" style="left:188px;top:14px">Our value proposition, based on delivering outcomes rather than just outputs, means that you receive the benefit and capability of deeply experienced corporate communications leaders without adding headcount or the time to identify, recruit, onboard and retain a new team member.</p>
    <p class="copy" style="left:29px;top:91px">We help organizations enhance their valuation by identifying areas that will appeal most to buyers and ensuring those elements of your business are visible and memorable to those who matter most.</p>
    <p class="copy" style="left:188px;top:91px">HarborLeap helps sellers maximize valuation and unlock hidden potential ahead of an exit- ensuring money is not left on the table.</p>
  </div>
  <div class="page-foot"></div>
</section>

</body>
</html>
```